Cancer Prevention

Heralds' Gardens is hosting a presentation by guest speaker Lena Varkosh, ND regarding cancer prevention April 29th, 2014 from 6:30pm until 7:30pm. There will be snacks and refreshments available during the presentation as well as questions answered following. There will be 3 door prizes given out at the conclusion of the presentation. Please incorporate a few of the pictures provided as well as a description of our speaker which is provided. Card must be 2-sided with the exception of the back right side to allow address and postage. Our address and phone number:
Heralds' Gardens
2745 W 38th St
Tulsa, OK 74119
918-526-3941

Please change the date to April 29th as we have moved the event to that date

We have moved the event to April 29th instead of April 22nd & the RSVP date should be changed to April 22nd. Please make the necessary adjustments to the postcards accordingly. Thank you

Font styles to use
Decorative
Script

Requirements
Must have
• Must have at least 5 or more of the provided photos total. The description of our speaker is also necessary, however if you choose to shorten it that is fine as well.
2-sided postcard with room on back right for address and postage. Must include "call 918-526-3941 to RSVP by April 22nd" somewhere in the card. Also, please include the fact that we will be giving door prizes away.

Heralds' Gardens
2745 W 38th St
Tulsa, OK 74119
918-526-3941
Also, please include placement of RSVP

```html
<!DOCTYPE html>
<html lang="en">
<head>
<meta charset="utf-8">
<title>Heralds' Gardens – Cancer Prevention Postcard</title>
<link href="https://fonts.googleapis.com/css2?family=Great+Vibes&family=Lora:ital,wght@0,400;0,700;1,400&display=swap" rel="stylesheet">
<style>
  :root{
    --page:#e9e6e2;
    --paper:#ffffff;
    --paper-shade:#f1eeee;
    --crimson:#a3161b;
    --crimson-soft:#c9545a;
    --maroon-top:#a55f5f;
    --maroon-mid:#6e2d30;
    --maroon-deep:#3c1517;
    --gold:#ecdca0;
    --gold-soft:#cdbb82;
    --cream:#f4ecd0;
    --partner-green:#b9c59a;
    --script:"Great Vibes", cursive;
    --serif:"Lora", Georgia, serif;
  }
  *{box-sizing:border-box;margin:0;padding:0}
  html,body{width:1200px;height:900px;overflow:hidden;background:var(--page)}
  .canvas{position:relative;width:1200px;height:900px}

  .postcard{position:absolute;top:236px;width:570px;height:428px;box-shadow:0 4px 14px rgba(0,0,0,.18);overflow:hidden}

  /* ---------- Front ---------- */
  .postcard--front{left:20px;background:linear-gradient(180deg,var(--paper) 70%,var(--paper-shade));font-family:var(--serif);color:var(--crimson)}
  .front__title{position:absolute;left:28px;top:8px;font-family:var(--script);font-size:46px;line-height:1.1;font-weight:400;white-space:nowrap}
  .front__subtitle{position:absolute;left:150px;top:62px;font-size:12px;line-height:1.2;letter-spacing:.12em;color:var(--crimson-soft)}
  .front__event{position:absolute;left:120px;top:80px;font-size:19px;line-height:1.2;font-weight:400}
  .front__date{position:absolute;left:120px;top:106px;font-size:10px;font-weight:700;line-height:1.35}
  .front__swoosh{position:absolute;left:100px;top:138px}
  .front__divider{position:absolute;left:262px;top:180px;width:2px;height:228px;background:#c7c2c2}
  .photo{position:absolute}
  .photo--lotion{left:30px;top:160px;width:100px;height:64px;background:linear-gradient(135deg,#b9a99a,#e7d7c7)}
  .photo--produce{left:30px;top:236px;width:68px;height:68px;border-radius:50%;background:radial-gradient(circle,#b9a25a,#6f7d3a)}
  .venn{position:absolute;left:128px;top:234px}
  .photo--exercise{left:88px;top:314px;width:108px;height:62px;background:linear-gradient(135deg,#3f5a2e,#7c8f58)}
  .front__rsvp{position:absolute;left:30px;top:386px;font-size:10px;line-height:1.3;font-weight:700}
  .front__address{position:absolute;left:30px;top:402px;font-size:10px;line-height:1.3;font-weight:700}
  .ribbon-faint{position:absolute;left:330px;top:250px;width:120px;height:150px;border-radius:40px;background:linear-gradient(160deg,rgba(0,0,0,.04),rgba(0,0,0,.01))}

  /* ---------- Back ---------- */
  .postcard--back{left:610px;background:linear-gradient(180deg,var(--maroon-top) 0%,var(--maroon-mid) 35%,var(--maroon-deep) 100%);font-family:var(--serif);color:var(--gold)}
  .ribbon{position:absolute;width:40px;height:64px;border-radius:14px;background:linear-gradient(160deg,var(--cream),var(--gold-soft))}
  .ribbon--left{left:26px;top:22px}
  .ribbon--right{right:22px;top:110px}
  .back__title{position:absolute;left:88px;top:8px;font-family:var(--script);font-size:44px;line-height:1.1;font-weight:400;white-space:nowrap}
  .back__subtitle{position:absolute;left:200px;top:58px;font-size:11px;line-height:1.2;letter-spacing:.14em}
  .back__event{position:absolute;left:0;right:0;top:84px;text-align:center;font-size:17px;line-height:1.2;font-weight:700}
  .back__date{position:absolute;left:0;right:0;top:110px;text-align:center;font-size:9.5px;font-weight:700;line-height:1.4}
  .speaker{position:absolute;left:20px;top:148px;width:398px;font-size:7.1px;line-height:1.32;color:var(--cream);text-align:justify}
  .speaker__portrait{float:left;width:94px;height:100px;margin:0 8px 4px 0;border:2px solid var(--gold-soft);position:relative;background:linear-gradient(180deg,#8a7a6c,#4e4038)}
  .speaker__caption{position:absolute;left:0;bottom:0;width:100%;background:#1d6b52;color:#fff;font-size:6.5px;padding:2px 3px;line-height:1.2}
  .speaker__welcome{font-size:9.5px;font-weight:700;color:var(--gold);margin-bottom:2px;line-height:1.2}
  .badge{position:absolute;left:438px;top:168px;width:84px;height:84px;border-radius:50%;border:2px solid var(--gold-soft);opacity:.7}
  .partner{position:absolute;left:432px;top:290px;width:118px;color:var(--partner-green)}
  .partner__name{display:flex;align-items:center;gap:6px;font-size:12px;line-height:1.15}
  .partner__dot{flex:none;width:18px;height:18px;border-radius:50%;background:#6c7d4c}
  .partner__tagline{font-size:6.5px;margin-top:8px;font-style:italic;color:#9da58a}
  .back__footer{position:absolute;left:0;right:0;top:392px;text-align:center;font-size:11.5px;line-height:1.2;font-weight:700;letter-spacing:.04em}
</style>
</head>
<body>
<main class="canvas">

  <section class="postcard postcard--front" aria-label="Postcard front">
    <h1 class="front__title">Heralds' Gardens</h1>
    <p class="front__subtitle">Assisted Living Facility</p>
    <h2 class="front__event">Cancer Prevention Presentation</h2>
    <p class="front__date">April 29th, 2014 from 6:30pm until 7:30pm<br>snacks, refreshments &amp; door prizes</p>
    <svg class="front__swoosh" width="170" height="16" viewBox="0 0 170 16" aria-hidden="true">
      <path d="M2 3 Q90 6 168 14" stroke="var(--crimson)" stroke-width="2.5" fill="none" stroke-linecap="round"/>
    </svg>

    <div class="photo photo--lotion" role="img" aria-label="Photo of sunscreen being applied to a shoulder"></div>
    <div class="photo photo--produce" role="img" aria-label="Photo of a circular plate of fruits and vegetables"></div>
    <svg class="venn" width="72" height="72" viewBox="0 0 76 76" role="img" aria-label="Three-circle prevention diagram">
      <circle cx="38" cy="38" r="37" fill="#2f6a55"/>
      <circle cx="31" cy="30" r="17" fill="#7fa9c9" opacity=".85"/>
      <circle cx="46" cy="30" r="17" fill="#9a7bc1" opacity=".85"/>
      <circle cx="38" cy="45" r="17" fill="#5b8fd0" opacity=".85"/>
    </svg>
    <div class="photo photo--exercise" role="img" aria-label="Photo of an older woman stretching outdoors"></div>

    <div class="front__divider"></div>
    <div class="ribbon-faint" role="img" aria-label="Faint awareness ribbon"></div>

    <p class="front__rsvp">call 918-526-3941 to RSVP by April 22nd</p>
    <p class="front__address">2745 W 38th St Tulsa, OK 74119</p>
  </section>

  <section class="postcard postcard--back" aria-label="Postcard back">
    <div class="ribbon ribbon--left" role="img" aria-label="Gold awareness ribbon"></div>
    <div class="ribbon ribbon--right" role="img" aria-label="Gold awareness ribbon"></div>
    <h1 class="back__title">Heralds' Gardens</h1>
    <p class="back__subtitle">Assisted Living Facility</p>
    <h2 class="back__event">Cancer Prevention Presentation</h2>
    <p class="back__date">April 29th, 2014 from 6:30pm until 7:30pm<br>snacks &amp; refreshments</p>

    <article class="speaker">
      <div class="speaker__portrait" role="img" aria-label="Portrait photo of the speaker">
        <span class="speaker__caption">Lena Varkosh<br>Naturopathic Provider</span>
      </div>
      <p class="speaker__welcome">Please join us in welcoming Lena Varkosh, ND</p>
      <p>Our guest speaker on cancer prevention April 29th, 2014 at 6:30pm. For years, Lena was interested in working with cancer patients, and knew she wanted to bring her focus on naturopathic medicine into an oncology setting. Riverstone Cancer Care provided an ideal environment for that goal. Varkosh obtained a doctorate in naturopathic medicine in 2012 at the Desert Ridge College of Natural Medicine in Tempe, Arizona. Immediately upon graduation, Varkosh joined RCC as a first-year resident, joining the team of comprehensive care providers at RCC's Oklahoma location. Varkosh obtained a bachelor of science, magna cum laude, at Laramie State University in 2008. She focused her studies on family and consumer sciences, with an emphasis on nutrition and food science. At Desert Ridge College of Natural Medicine, Varkosh completed accredited programs in botanical, nutritional, homeopathic, Oriental, and physical medicine, as well as in hydrotherapy. She also dedicated extensive study to integrative oncology. She is affiliated with the Integrative Oncology Circle, the National Guild of Natural Practitioners, and the Prairie Society of Natural Health. She is certified in Reiki levels 1 and 2. She has devoted her spare time to volunteering with the Bright Hopes Foundation, the Little Stars Network, and with local senior facilities.</p>
    </article>

    <div class="badge" role="img" aria-label="Professional association badge"></div>
    <div class="partner">
      <div class="partner__name"><span class="partner__dot"></span><span>Riverstone Cancer Care</span></div>
      <p class="partner__tagline">Standing with patients every day.</p>
    </div>

    <p class="back__footer">2745 W 38th St Tulsa, OK 74119 &nbsp;|&nbsp; 918-526-3941</p>
  </section>

</main>
</body>
</html>
```